Brume vodka

With the logo attached in the subsequent file, a business card that reflects a premium and organic vodka. On the first side, the company logo in large. The names must be included on the back of the card (Miguel Ángel Tomás Ferrandis with the number +34 655 271 389 and Pau Berenguer Casals and +34 677 314 920). The slogan "What binds us" and "Organic and permium vodka" in bold E-mail (brumevodka@mailfield.net); Website www.brumevodkaorg.net

```html
<!DOCTYPE html>
<html lang="en">
<head>
<meta charset="utf-8">
<title>Brume vodka – business card</title>
<link rel="stylesheet" href="https://fonts.googleapis.com/css2?family=Source+Sans+3:wght@400;600&family=EB+Garamond:ital@1&display=swap">
<style>
  :root {
    --backdrop: #e6e3de;
    --card-white: #ffffff;
    --card-grey: #808080;
    --band-grey: #b3b4b6;
    --ink-grey: #848484;
    --ink-dark: #555555;
    --ink-white: #ffffff;
  }
  * { margin: 0; padding: 0; box-sizing: border-box; }
  html, body { width: 1200px; height: 1040px; overflow: hidden; }
  body {
    background: var(--backdrop);
    font-family: "Source Sans 3", Arial, sans-serif;
    position: relative;
  }
  .card {
    position: absolute;
    left: 285px;
    width: 640px;
    height: 365px;
    overflow: hidden;
    box-shadow: 0 3px 8px rgba(0,0,0,0.25);
  }
  .card--front { top: 130px; background: var(--card-white); }
  .card--back  { top: 567px; background: var(--card-grey); }

  .brand-name {
    position: absolute;
    font-family: "Source Sans 3", Arial, sans-serif;
    font-weight: 400;
    white-space: nowrap;
  }
  .card--front .brand-name {
    left: 43px; top: 62px;
    font-size: 46px;
    color: var(--ink-grey);
    letter-spacing: 1px;
  }
  .card--back .brand-name {
    left: 0; right: 0; top: 165px;
    text-align: center;
    font-size: 64px;
    color: var(--ink-white);
    letter-spacing: 2px;
  }

  .contacts {
    position: absolute;
    right: 34px; top: 42px;
    text-align: right;
    color: var(--ink-dark);
  }
  .contact { margin-bottom: 11px; }
  .contact__name {
    font-weight: 600;
    font-size: 17px;
    color: var(--ink-grey);
    line-height: 22px;
  }
  .contact__phone { font-size: 16px; line-height: 22px; }

  .address {
    position: absolute;
    left: 43px; top: 212px;
    font-size: 15.5px;
    line-height: 21px;
    color: var(--ink-dark);
  }
  .links {
    position: absolute;
    left: 41px; top: 267px;
    font-size: 15.5px;
    line-height: 21px;
    color: var(--ink-dark);
    list-style: none;
  }
  .links li { display: flex; align-items: center; gap: 9px; }
  .links svg { width: 14px; height: 14px; flex: none; }

  .band { position: absolute; left: 0; bottom: 0; width: 640px; height: 50px; }
  .slogan {
    position: absolute;
    left: 0; right: 0;
    text-align: center;
    font-family: "EB Garamond", Georgia, serif;
    font-style: italic;
    white-space: nowrap;
  }
  .card--front .slogan { bottom: 10px; padding-left: 138px; font-size: 17px; color: var(--ink-white); }
  .card--back .slogan  { bottom: 11px; font-size: 18px; color: var(--ink-dark); }
</style>
</head>
<body>

<section class="card card--front" aria-label="Card front">
  <div class="brand-name">Brume vodka</div>

  <div class="contacts">
    <div class="contact">
      <div class="contact__name">Pau Berenguer Casals</div>
      <div class="contact__phone">+34 677 314 920</div>
    </div>
    <div class="contact">
      <div class="contact__name">Miguel Ángel Tomás Ferrandis</div>
      <div class="contact__phone">+34 655 271 389</div>
    </div>
  </div>

  <address class="address" style="font-style:normal">
    Carrer Nou 48 ENTLO. 2<br>
    Barcelona, 08012 Spain
  </address>

  <ul class="links">
    <li>
      <svg viewBox="0 0 14 14" aria-hidden="true">
        <rect x="1" y="3" width="12" height="8" fill="var(--ink-grey)"/>
        <path d="M1 3 L7 8 L13 3" fill="none" stroke="#ffffff" stroke-width="1.2"/>
      </svg>
      brumevodka@mailfield.net
    </li>
    <li>
      <svg viewBox="0 0 14 14" aria-hidden="true">
        <circle cx="7" cy="7" r="6" fill="var(--ink-grey)"/>
        <path d="M4 4.5 Q6 5 6.5 7 Q5 9 6 11 M9 3.5 Q8 6 10 7.5" fill="none" stroke="#ffffff" stroke-width="1.1"/>
      </svg>
      www.brumevodkaorg.net
    </li>
  </ul>

  <svg class="band" viewBox="0 0 640 50" preserveAspectRatio="none" aria-hidden="true">
    <path d="M0 40 Q320 -10 640 43 L640 50 L0 50 Z" fill="var(--band-grey)"/>
  </svg>
  <div class="slogan">What Binds us</div>
</section>

<section class="card card--back" aria-label="Card back">
  <div class="brand-name">Brume vodka</div>

  <svg class="band" viewBox="0 0 640 50" preserveAspectRatio="none" aria-hidden="true">
    <path d="M0 46 Q320 -18 640 38 L640 50 L0 50 Z" fill="var(--card-white)"/>
  </svg>
  <div class="slogan">Organic &amp; permium vodka</div>
</section>

</body>
</html>
```